Vorel constructions

We are predominantly a residential home builder based in Melbourne, Victoria Australia. We construct houses, apartments, townhouses, multi-unit developments.

The name of the company is "Vorel Constructions"
My company believes in building unique construction projects mainly residential homes. The target customers are upmarket Melbourne residents/investors.

I want the brand name "Vorel" to be part of the logo. There's no need to put the word construction in the logo at this stage.

I would also like some ideas for a slogan e.g. "Just build it." or "We build quality homes." But I would like something unique and different for a slogan not the same old cliche.

vorelconstructions.example.com.au
e: tmelo@vorelconstructions.example.com.au
M: 0417305862
Address: 8/3 Fenwick Lane Clayton VIC 3168

Director:Mr Dinesh Malarkodiyan

```html
<!DOCTYPE html>
<html lang="en">
<head>
<meta charset="UTF-8">
<title>Vorel Constructions — Business Card</title>
<link href="https://fonts.googleapis.com/css2?family=Questrial&family=Oswald:wght@500&display=swap" rel="stylesheet">
<style>
  :root {
    --page-bg: #e4e4e8;
    --card-bg: #2b2540;
    --card-bg-deep: #221d34;
    --cyan: #1fb8ea;
    --cyan-dark: #1283b8;
    --white: #ffffff;
    --muted: #d9d6e4;
    --badge: #f2f2f4;
  }
  * { margin: 0; padding: 0; box-sizing: border-box; }
  html, body { width: 1200px; height: 3000px; overflow: hidden; }
  body {
    background: var(--page-bg);
    position: relative;
    font-family: "Questrial", sans-serif;
  }
  .card {
    position: absolute;
    left: 80px;
    width: 1040px;
    height: 634px;
    border-radius: 26px;
    background: linear-gradient(135deg, var(--card-bg) 0%, var(--card-bg-deep) 100%);
    overflow: hidden;
  }
  .card-front { top: 640px; }
  .card-back { top: 1640px; }

  /* Front */
  .brand {
    position: absolute;
    left: 90px;
    top: 230px;
    display: flex;
    align-items: center;
    gap: 22px;
  }
  .brand-square {
    width: 34px;
    height: 34px;
    background: var(--cyan);
  }
  .brand-name {
    font-family: "Questrial", sans-serif;
    font-size: 104px;
    line-height: 1;
    color: var(--cyan);
    letter-spacing: 2px;
  }
  .divider {
    position: absolute;
    left: 540px;
    top: 86px;
    width: 2px;
    height: 116px;
    background: var(--white);
  }
  .details {
    position: absolute;
    left: 566px;
    top: 84px;
    right: 30px;
  }
  .person-name {
    font-family: "Oswald", sans-serif;
    font-weight: 500;
    font-size: 28px;
    color: var(--white);
    letter-spacing: 1px;
    text-transform: uppercase;
    white-space: nowrap;
  }
  .person-role {
    font-size: 26px;
    color: var(--cyan);
    margin-top: 4px;
  }
  .contact-list {
    list-style: none;
    margin-top: 34px;
  }
  .contact-item {
    display: flex;
    align-items: center;
    gap: 14px;
    font-size: 21px;
    color: var(--muted);
    margin-bottom: 12px;
    white-space: nowrap;
  }
  .contact-icon {
    width: 24px;
    height: 24px;
    flex: none;
  }
  .slogan {
    margin-top: 30px;
    font-size: 30px;
    line-height: 1.08;
  }
  .slogan-lead { color: var(--cyan); display: block; }
  .slogan-tail { color: var(--white); display: block; }
  .rule-cyan {
    position: absolute;
    left: 0;
    top: 508px;
    width: 720px;
    height: 9px;
    background: var(--cyan);
  }
  .rule-white {
    position: absolute;
    left: 0;
    top: 534px;
    width: 720px;
    height: 4px;
    background: var(--white);
  }

  /* Back */
  .back-stripes {
    position: absolute;
    inset: 0;
    width: 100%;
    height: 100%;
  }
  .badge {
    position: absolute;
    right: 60px;
    bottom: 60px;
    width: 180px;
    height: 110px;
    border-radius: 8px;
    background: var(--badge);
  }
</style>
</head>
<body>

  <section class="card card-front" aria-label="Business card front">
    <div class="brand">
      <span class="brand-square"></span>
      <span class="brand-name">Vorel</span>
    </div>

    <div class="divider"></div>

    <div class="details">
      <p class="person-name">Mr Dinesh Malarkodiyan</p>
      <p class="person-role">Director</p>

      <ul class="contact-list">
        <li class="contact-item">
          <svg class="contact-icon" viewBox="0 0 24 24">
            <rect width="24" height="24" rx="3" fill="#ffffff"/>
            <path d="M8 5h3l1 4-2 1a8 8 0 0 0 4 4l1-2 4 1v3a2 2 0 0 1-2 2A12 12 0 0 1 6 7a2 2 0 0 1 2-2z" fill="#2b2540"/>
          </svg>
          0417305862
        </li>
        <li class="contact-item">
          <svg class="contact-icon" viewBox="0 0 24 24">
            <rect width="24" height="24" rx="3" fill="#ffffff"/>
            <rect x="5" y="7" width="14" height="10" fill="none" stroke="#2b2540" stroke-width="2"/>
            <path d="M5 7l7 6 7-6" fill="none" stroke="#2b2540" stroke-width="2"/>
          </svg>
          tmelo@vorelconstructions.example.com.au
        </li>
        <li class="contact-item">
          <svg class="contact-icon" viewBox="0 0 24 24">
            <rect width="24" height="24" rx="3" fill="#ffffff"/>
            <circle cx="12" cy="12" r="6.5" fill="none" stroke="#2b2540" stroke-width="2"/>
            <path d="M5.5 12h13M12 5.5c-3 3.5-3 9.5 0 13M12 5.5c3 3.5 3 9.5 0 13" fill="none" stroke="#2b2540" stroke-width="1.5"/>
          </svg>
          vorelconstructions.example.com.au
        </li>
        <li class="contact-item">
          <svg class="contact-icon" viewBox="0 0 24 24">
            <rect width="24" height="24" rx="3" fill="#ffffff"/>
            <path d="M12 19s-5-5.5-5-9a5 5 0 0 1 10 0c0 3.5-5 9-5 9z" fill="#2b2540"/>
            <circle cx="12" cy="10" r="2" fill="#ffffff"/>
          </svg>
          8/3 Fenwick Lane Norbury VIC 3291
        </li>
      </ul>

      <p class="slogan">
        <span class="slogan-lead">We build with</span>
        <span class="slogan-tail">vorelness and passion</span>
      </p>
    </div>

    <div class="rule-cyan"></div>
    <div class="rule-white"></div>
  </section>

  <section class="card card-back" aria-label="Business card back">
    <svg class="back-stripes" viewBox="0 0 1040 634" preserveAspectRatio="none">
      <polygon points="560,0 700,0 380,634 240,634" fill="#1283b8"/>
      <polygon points="720,0 800,0 480,634 400,634" fill="#ffffff"/>
      <polygon points="820,0 1040,0 1040,120 720,634 500,634" fill="#1fb8ea"/>
      <polygon points="1040,160 1040,634 760,634" fill="#1283b8"/>
    </svg>
    <div class="badge"></div>
  </section>

</body>
</html>
```